Website to help people naturally reverse diabetes

Wordpress designed with elementor. it is less than 5 pages.
we help people naturally reverse their disease diabetes.
this is my domain www.bluemeadowpath.care

(my original website was www.kestrelhollow.care
but we are creating different website for different disease condition starting with diabetes.)

1. home page and with a scheduling option
2. blog page
3. Coach page
4. Contact us

Target Market(s)

1.mid age to older people mostly that are diabetic and it is mostly the American citizens but will be used internationally

Industry/Entity Type

Health care

Coding

Number of Pages Required

4 page

Colors
0054AA
0677BA
7BADD7
CADEEF
E8F1F8
00AB8E
00BBA5
67D7C9
C6EFE9
E9F9F6
A7469A
B969AE
D3A5CF
EDDBEB
F8F0F9
6B429C
8869AF
B7A5CE
E3DAEB
F3F0F8

Requirements
Must have
• clean and good fee.l lumen arc concept a. make the customer the hero. the header page picture should reveal what the customer will feel after the program. Treating the symptom I attached a picture in the file a screen shot.. Normally people treat the symptoms and not the cause. that is 1. closing the tap. 2. remove the block. 3 and them clean he spill over. but do not want to have the picture of medical doctor or nurse. I do not want to offend them we can use the same picture but without them but some way we want to communicate the message.
Nice to have
• more visual feel

```html
<!DOCTYPE html>
<html lang="en">
<head>
<meta charset="utf-8">
<title>Kestrel Hollow – Reverse Type 2 Diabetes</title>
<link href="https://fonts.googleapis.com/css2?family=Poppins:wght@400;500;600;700&display=swap" rel="stylesheet">
<style>
:root{
  --green:#61b744;
  --green-dark:#4fa033;
  --navy:#1c2350;
  --nav-bg:#22305f;
  --text:#3b3f52;
  --muted:#6b6f80;
  --soft:#f4f5f7;
  --line:#e3e5ea;
  --footer:#232323;
  --white:#ffffff;
}
*{box-sizing:border-box;margin:0;padding:0}
html,body{width:1200px;height:1200px;overflow:hidden}
body{background:#ffffff;font-family:"Poppins",sans-serif;color:var(--text);position:relative}
.page{position:absolute;width:552px;background:var(--white);box-shadow:0 4px 18px rgba(0,0,0,.18);overflow:hidden;display:flex;flex-direction:column}
.page--home-top{left:30px;top:35px;height:1165px}
.page--home-bottom{left:617px;top:0;height:1077px}
section,header,nav,footer{flex:none;position:relative}
.btn{display:inline-block;background:var(--green);color:#fff;font-size:5.5px;font-weight:600;letter-spacing:.3px;padding:7px 12px;text-transform:uppercase;border-radius:1px}
.btn--light{background:#fff;color:var(--navy)}
.h-sec{font-size:16px;font-weight:500;color:var(--navy);text-align:center;line-height:1.25;text-transform:uppercase}
.tiny{font-size:5px;line-height:1.55;color:var(--muted)}
.center{text-align:center}

/* header */
.site-header{height:37px;display:flex;align-items:center;justify-content:space-between;padding:0 42px 0 40px}
.brand{display:flex;align-items:center;gap:5px}
.brand__dot{width:13px;height:13px;border-radius:50%;background:var(--green)}
.brand__name{font-size:7px;font-weight:700;color:var(--navy);letter-spacing:.2px;line-height:1.1}
.header-contact{display:flex;align-items:center;gap:8px}
.header-contact__icon{width:20px;height:20px;border:1.5px solid var(--green);border-radius:50%;display:flex;align-items:center;justify-content:center}
.header-contact__url{font-size:5.5px;color:var(--green);font-weight:500}
.header-contact .btn{padding:7px 14px;margin-left:6px}
.main-nav{height:22px;background:var(--nav-bg);display:flex;align-items:center;padding-left:74px;gap:23px}
.main-nav a{color:#fff;font-size:5.3px;text-decoration:none;font-weight:500}

/* hero */
.hero{height:226px;background:linear-gradient(100deg,#5a4a3e 0%,#8e7462 35%,#b89a82 60%,#d8c6b4 100%);display:flex;flex-direction:column;align-items:center;justify-content:center;color:#fff;text-align:center}
.hero::before{content:"";position:absolute;inset:0;background:rgba(20,20,30,.35)}
.hero > *{position:relative}
.hero__title{font-size:16px;font-weight:500;line-height:1.3;text-transform:uppercase;margin-top:18px}
.hero__title em{font-style:normal;color:var(--green)}
.hero__sub{font-size:7px;line-height:1.45;margin:6px 0 14px}
.hero__dots{position:absolute;bottom:6px;left:50%;transform:translateX(-50%);display:flex;gap:3px;align-items:center}
.hero__dots span{width:4px;height:4px;border-radius:50%;background:#fff}
.hero__dots .on{width:16px;border-radius:3px}

/* medication */
.medication{height:329px;background:var(--soft);padding-top:14px}
.medication__lead{font-size:7px;text-align:center;color:var(--text);line-height:1.45;margin-top:4px}
.medication__body{display:flex;gap:14px;padding:0 40px 0 43px;margin-top:14px}
.medication__photo{width:227px;height:205px;border-radius:3px;background:linear-gradient(160deg,#8fb3bd,#5d8e9b 55%,#3f6f7d)}
.relate{padding-top:20px;width:230px}
.relate__title{font-size:9px;font-weight:600;color:var(--navy);margin-bottom:8px}
.relate__item{display:flex;gap:5px;font-size:4.8px;line-height:1.55;color:var(--text);text-transform:uppercase;margin-bottom:8px}
.tick{flex:none;width:8px;height:8px;border-radius:50%;background:var(--green);display:flex;align-items:center;justify-content:center}

/* service */
.service{height:208px;padding-top:14px;text-align:center}
.service__title{font-size:18px;font-weight:500;color:var(--navy)}
.service__sub{font-size:6px;line-height:1.5;margin-top:2px}
.service__row{display:flex;justify-content:center;gap:40px;margin:12px 0 12px}
.service__item{width:100px}
.service__icon{width:38px;height:38px;border:1.5px solid var(--green);border-radius:50%;margin:0 auto 6px;display:flex;align-items:center;justify-content:center}
.service__name{font-size:7px;font-weight:600;color:var(--navy);margin-bottom:3px}

/* results */
.results-head{height:54px;display:flex;align-items:center;justify-content:center}
.results{height:235px;background:var(--soft);display:grid;grid-template-columns:repeat(3,1fr);padding:12px 50px 0;row-gap:10px}
.result{text-align:center}
.result__icon{width:56px;height:56px;border-radius:50%;background:var(--green);margin:0 auto 5px;display:flex;align-items:center;justify-content:center}
.result__name{font-size:7.5px;font-weight:600;color:var(--navy);text-transform:uppercase}
.result__name--mixed{text-transform:none}
.result__pct{font-size:7px;color:var(--green);font-weight:500}
.result__base{font-size:6px;color:var(--green)}

/* steps */
.steps-peek{padding-top:12px}
.steps{height:180px;padding-top:12px;text-align:center}
.steps__row{display:flex;justify-content:center;gap:20px;margin:8px 0 10px}
.step{width:135px}
.step__num{font-size:26px;font-weight:500;color:var(--navy);line-height:1}
.step__title{font-size:6.5px;font-weight:600;color:var(--navy);text-transform:uppercase;line-height:1.3;margin:3px 0 4px}

/* testimonials */
.testimonials{height:200px;background:var(--soft);padding-top:12px;text-align:center}
.testimonials__quote{font-size:14px}
.testimonials__row{display:flex;justify-content:center;gap:20px;margin-top:12px}
.person{width:135px}
.person__avatar{width:52px;height:52px;border-radius:50%;margin:0 auto 6px;border:2px solid #fff}
.person__avatar--a{background:linear-gradient(135deg,#6a5a52,#3c3432)}
.person__avatar--b{background:linear-gradient(135deg,#7fc0d6,#c49a7e)}
.person__avatar--c{background:linear-gradient(135deg,#8b5e4b,#d8b39a)}
.person__name{font-size:6.5px;font-weight:600;color:var(--navy);margin-bottom:2px}

/* method */
.method{height:257px;padding-top:14px;text-align:center}
.method__ways{font-size:8px;font-weight:500;color:var(--navy);margin:6px 0 10px}
.method__cols{display:flex;justify-content:center;gap:16px;text-align:left;margin-bottom:12px}
.plan{width:140px}
.plan__title{font-size:6px;font-weight:600;color:var(--navy);margin-bottom:2px}
.plan p,.plan li{font-size:4.6px;line-height:1.6;color:var(--text);text-transform:uppercase}
.plan ul{list-style:none}
.plan li::before{content:". "}

/* cta */
.cta{height:197px;background:linear-gradient(110deg,#6b7a86,#a9b3bb 45%,#8a949d 75%,#5e6a74);color:#fff;text-align:center;padding-top:22px}
.cta::before{content:"";position:absolute;inset:0;background:rgba(25,35,55,.45)}
.cta > *{position:relative}
.cta__title{font-size:14px;font-weight:500;line-height:1.25;text-transform:uppercase}
.cta__text{font-size:6px;line-height:1.7;margin:8px auto 12px;width:420px}

/* signup */
.signup{height:106px;text-align:center;padding-top:14px}
.signup__title{font-size:12.5px;font-weight:500;color:var(--navy);line-height:1.3}
.signup__form{display:flex;justify-content:center;gap:10px;margin-top:14px}
.field{width:94px;height:24px;border:1px solid var(--line);background:#fafafa;font-size:5px;color:var(--text);text-align:left;padding:9px 8px}
.signup__form .btn{width:94px;height:24px;text-align:center;padding:9px 0}

/* footer */
.site-footer{height:137px;background:var(--footer);color:#cfcfcf;display:grid;grid-template-columns:92px 62px 72px 118px 1fr;gap:10px;padding:12px 16px 0 40px}
.foot-brand{text-align:center}
.foot-brand .brand__dot{margin:0 auto 3px}
.foot-brand .brand__name{color:#fff;font-size:5.5px;margin-bottom:4px}
.site-footer .tiny{color:#c8c8c8;font-size:4.5px}
.foot-title{font-size:7px;font-weight:600;color:#fff;margin-bottom:6px}
.foot-list{list-style:none}
.foot-list li{font-size:4.5px;line-height:2}
.cards{display:flex;gap:3px;margin-top:6px;justify-content:center}
.cards span{width:11px;height:7px;background:#777;border-radius:1px}
.news-input{width:70px;height:14px;background:#fff;font-size:4.5px;color:#555;padding:4px 5px;margin:8px 0}
.socials{display:flex;gap:5px}
.socials span{width:9px;height:9px;border-radius:50%;background:#ddd}
.socials span.on{background:var(--green)}
.copy{position:absolute;bottom:8px;left:0;right:0;text-align:center;font-size:4.2px;color:#aaa}
.foot-label{font-size:6px;font-weight:600;color:#fff}
.foot-phone{font-size:6.5px;color:#fff;font-weight:600;margin:3px 0}
</style>
</head>
<body>

<main class="page page--home-top">
  <header class="site-header">
    <div class="brand">
      <span class="brand__dot"></span>
      <span class="brand__name">KESTREL HOLLOW</span>
    </div>
    <div class="header-contact">
      <span class="header-contact__icon">
        <svg width="10" height="8" viewBox="0 0 10 8"><rect x=".5" y=".5" width="9" height="7" fill="none" stroke="#61b744"/><path d="M.5 .8 5 4.5 9.5 .8" fill="none" stroke="#61b744"/></svg>
      </span>
      <span class="header-contact__url">www.kestrelhollow.care</span>
      <span class="btn">Schedule a call</span>
    </div>
  </header>

  <nav class="main-nav">
    <a>HOME</a><a>ABOUT</a><a>SERVICE</a><a>BEATING DIABETES</a><a>TESTIMONIAL</a><a>METHOD</a><a>OUR APPROACH</a><a>CONTACT</a>
  </nav>

  <section class="hero" role="img" aria-label="Photo of a smiling family with a child during a friendly check-up">
    <h1 class="hero__title">We <em>give people</em> their lives back<br>by reversing <em>type 2 diabetes</em></h1>
    <p class="hero__sub">A 12-week lifestyle-coaching program scientifically<br>proven to restore your health and be medication free.</p>
    <span class="btn btn--light">Schedule a call</span>
    <div class="hero__dots"><span></span><span></span><span class="on"></span><span></span><span></span></div>
  </section>

  <section class="medication">
    <h2 class="h-sec">You shouldn’t have to be on<br>medication for the rest of your life</h2>
    <p class="medication__lead">Not only is it expensive, but it can cause serious long-term<br>side effects like obesity, cancer and cardiovascular disease.</p>
    <div class="medication__body">
      <div class="medication__photo" role="img" aria-label="Photo of a care team standing together in a clinic"></div>
      <div class="relate">
        <h3 class="relate__title">CAN YOU RELATE?</h3>
        <div class="relate__item"><span class="tick"><svg width="5" height="4" viewBox="0 0 5 4"><path d="M.5 2 2 3.3 4.5.7" fill="none" stroke="#fff" stroke-width=".9"/></svg></span>You feel like you’re just chasing your symptoms with medication after medication.</div>
        <div class="relate__item"><span class="tick"><svg width="5" height="4" viewBox="0 0 5 4"><path d="M.5 2 2 3.3 4.5.7" fill="none" stroke="#fff" stroke-width=".9"/></svg></span>Your medical expenses have continued to increase, but your health has stayed the same or gotten worse.</div>
        <div class="relate__item"><span class="tick"><svg width="5" height="4" viewBox="0 0 5 4"><path d="M.5 2 2 3.3 4.5.7" fill="none" stroke="#fff" stroke-width=".9"/></svg></span>Your medical expenses have continued to increase, but your health has stayed the same or gotten worse.</div>
        <div class="relate__item"><span class="tick"><svg width="5" height="4" viewBox="0 0 5 4"><path d="M.5 2 2 3.3 4.5.7" fill="none" stroke="#fff" stroke-width=".9"/></svg></span>You dread the thought of leaving your family behind — and in the meantime, burdening them with your declining health.</div>
        <span class="btn" style="margin-top:4px">Schedule a call</span>
      </div>
    </div>
  </section>

  <section class="service">
    <h2 class="service__title">Our Service</h2>
    <p class="service__sub">You deserve a plan that will get you back to optimal<br>Health with the support of professionals who care.</p>
    <div class="service__row">
      <div class="service__item">
        <div class="service__icon"><svg width="16" height="18" viewBox="0 0 16 18"><rect x="3" y="1" width="10" height="16" rx="1.5" fill="none" stroke="#61b744" stroke-width="1.3"/><path d="M8 6v6M6 8h3.5a1 1 0 0 1 0 2H6.5" fill="none" stroke="#61b744" stroke-width="1.1"/></svg></div>
        <div class="service__name">Save Money</div>
        <p class="tiny">Say goodbye to expensive treatments and doctor visits with lifestyle changes that actually work.</p>
      </div>
      <div class="service__item">
        <div class="service__icon"><svg width="18" height="16" viewBox="0 0 18 16"><path d="M9 15 2 8a4 4 0 0 1 7-5 4 4 0 0 1 7 5z" fill="#61b744"/><circle cx="9" cy="7" r="2" fill="#fff"/></svg></div>
        <div class="service__name">End Insulin Dependence</div>
        <p class="tiny">We’ll teach you how to control your blood glucose levels and restore your health – naturally.</p>
      </div>
      <div class="service__item">
        <div class="service__icon"><svg width="18" height="16" viewBox="0 0 18 16"><path d="M9 15 2 8a4 4 0 0 1 7-5 4 4 0 0 1 7 5z" fill="none" stroke="#61b744" stroke-width="1.3"/><path d="M4 8h3l1-2 2 4 1-2h3" fill="none" stroke="#61b744" stroke-width="1"/></svg></div>
        <div class="service__name">Feel the Difference</div>
        <p class="tiny">Most people see improvements in energy, mood, and symptoms within the first month.</p>
      </div>
    </div>
    <span class="btn">Schedule a call</span>
  </section>

  <section class="results-head">
    <h2 class="h-sec">Extraordinary results in our<br>highest risk patients</h2>
  </section>

  <section class="results">
    <div class="result">
      <div class="result__icon"><svg width="24" height="24" viewBox="0 0 24 24"><rect x="4" y="6" width="16" height="12" rx="2" fill="none" stroke="#fff" stroke-width="1.6"/><path d="M7 14l3-3 3 2 4-4" fill="none" stroke="#fff" stroke-width="1.6"/></svg></div>
      <div class="result__name">Triglycerides</div><div class="result__pct">44.1% decline</div><div class="result__base">Initial level: Above 500mg/dl</div>
    </div>
    <div class="result">
      <div class="result__icon"><svg width="24" height="24" viewBox="0 0 24 24"><path d="M7 3v7a5 5 0 0 0 10 0V3M12 15v3a3 3 0 0 0 6 0" fill="none" stroke="#fff" stroke-width="1.6"/><circle cx="18" cy="16" r="1.8" fill="#fff"/></svg></div>
      <div class="result__name result__name--mixed">Fasting Plasma Glucose</div><div class="result__pct">19.5% decline</div><div class="result__base">Initial level: Above 500mg/dl</div>
    </div>
    <div class="result">
      <div class="result__icon"><svg width="24" height="24" viewBox="0 0 24 24"><path d="M12 21 3.5 12.5a5 5 0 0 1 8.5-6 5 5 0 0 1 8.5 6z" fill="#fff"/><path d="M12 9v6M9 12h6" stroke="#61b744" stroke-width="1.8"/></svg></div>
      <div class="result__name">Total Cholestroal</div><div class="result__pct">19.8% decline</div><div class="result__base">Initial level: Above 500mg/dl</div>
    </div>
    <div class="result">
      <div class="result__icon"><svg width="24" height="24" viewBox="0 0 24 24"><path d="M12 12 7 7a3 3 0 0 1 5-3 3 3 0 0 1 5 3z" fill="none" stroke="#fff" stroke-width="1.5"/><path d="M4 13v5l4 3h4M20 13v5l-4 3h-4" fill="none" stroke="#fff" stroke-width="1.5"/></svg></div>
      <div class="result__name">LDL Cholestroal</div><div class="result__pct">16.1% decline</div><div class="result__base">Initial level: Above 500mg/dl</div>
    </div>
    <div class="result">
      <div class="result__icon"><svg width="24" height="24" viewBox="0 0 24 24"><path d="M12 3 19 6v6c0 4-3 7-7 9-4-2-7-5-7-9V6z" fill="none" stroke="#fff" stroke-width="1.5"/><circle cx="12" cy="12" r="3" fill="none" stroke="#fff" stroke-width="1.5"/></svg></div>
      <div class="result__name">Sydromine Sydrome</div><div class="result__pct">45.1% decline</div><div class="result__base">Initial level: Above 500mg/dl</div>
    </div>
    <div class="result">
      <div class="result__icon"><svg width="24" height="24" viewBox="0 0 24 24"><rect x="9" y="3" width="5" height="13" rx="2.5" fill="none" stroke="#fff" stroke-width="1.5"/><circle cx="11.5" cy="18" r="3.2" fill="#fff"/><path d="M16 6h3M16 9h2M16 12h3" stroke="#fff" stroke-width="1.2"/></svg></div>
      <div class="result__name">Body Mass Index</div><div class="result__pct">50.1% decline</div><div class="result__base">Initial level: Above 500mg/dl</div>
    </div>
  </section>

  <section class="steps-peek center">
    <h2 class="h-sec">Just three steps to beating diabetes</h2>
    <div class="steps__row"><div class="step step__num">1</div><div class="step step__num">2</div><div class="step step__num">3</div></div>
  </section>
</main>

<main class="page page--home-bottom">
  <section class="steps">
    <h2 class="h-sec">Just three steps to beating diabetes</h2>
    <div class="steps__row">
      <div class="step"><div class="step__num">1</div><div class="step__title">Schedule free<br>discovery call</div><p class="tiny">We will talk with you about your health, lifestyle habits, and the issues you are facing and find out what barriers you’re struggling with. Together, we’ll decide if this is the right program for you.</p></div>
      <div class="step"><div class="step__num">2</div><div class="step__title">Get your<br>customized plan</div><p class="tiny">Our physician and dietitian will create a lifestyle and diet plan to help you eliminate your diabetes. We take into consideration your unique situation, and then work with you to help you get the outcome you want.</p></div>
      <div class="step"><div class="step__num">3</div><div class="step__title">Enjoy a happier &amp;<br>healthier life</div><p class="tiny">Your personal lifestyle coach will assist you for 12 weeks toward a healthier life transformation. Not only will you lose weight, look younger, and have more energy, you’ll live a longer life.</p></div>
    </div>
    <span class="btn">Schedule a call</span>
  </section>

  <section class="testimonials">
    <h2 class="h-sec testimonials__quote">“After just 45 days in the program<br>I’m insulin free and my life<br>is back to normal!”</h2>
    <div class="testimonials__row">
      <div class="person"><div class="person__avatar person__avatar--a" role="img" aria-label="Portrait photo of a program member"></div><div class="person__name">MARTIN E. HALE</div><p class="tiny">My sugar numbers finally settled, and I feel stronger, calmer and more hopeful every week.</p></div>
      <div class="person"><div class="person__avatar person__avatar--b" role="img" aria-label="Portrait photo of a program member"></div><div class="person__name">OWEN T. REYES</div><p class="tiny">The coaching made small daily changes easy, and my energy came back within one month.</p></div>
      <div class="person"><div class="person__avatar person__avatar--c" role="img" aria-label="Portrait photo of a program member"></div><div class="person__name">CLARA J. MOSS</div><p class="tiny">I cook real food again, walk each morning and no longer fear my next check-up results.</p></div>
    </div>
  </section>

  <section class="method">
    <h2 class="h-sec">Our proven lifestyle coaching method<br>works from the inside out.</h2>
    <p class="method__ways">THERE ARE 3 WAYS TO WORK WITH US:</p>
    <div class="method__cols">
      <div class="plan">
        <div class="plan__title">1:1 DIABETIC COACHING</div>
        <p>Health information alone does not change people. But magic happens when you couple the right information with an experience</p>
        <ul><li>Personalized coach</li><li>Doctor and nutritionist support</li><li>12 coaching sessions</li><li>18 educational sessions &amp; workbook</li><li>Cookbook</li><li>Exercise book</li><li>App for messaging your coach</li><li>24/7 access to all resources for year</li></ul>
      </div>
      <div class="plan">
        <div class="plan__title">GROUP DIABETIC COACHING</div>
        <p>Enjoy a community of people who are the journey of our additional connection and support.</p>
        <ul><li>Personalized coach</li><li>Doctor and nutritionist support</li><li>12 coaching sessions</li><li>18 educational sessions &amp; workbook</li><li>Cookbook</li><li>Exercise book</li><li>App for messaging your coach</li><li>24/7 access to all resources for year</li></ul>
      </div>
      <div class="plan">
        <div class="plan__title">ONLINE DIABETIC COURSE</div>
        <p>Over 21 days you’ll empower yourself to address the root cause of diabetes and integrate your transformation at your</p>
        <ul><li>Personalized coach</li><li>Doctor and nutritionist support</li><li>12 coaching sessions</li><li>18 educational sessions &amp; workbook</li><li>Cookbook</li><li>Exercise book</li><li>App for messaging your coach</li><li>24/7 access to all resources for year</li></ul>
      </div>
    </div>
    <span class="btn">Schedule a call</span>
  </section>

  <section class="cta" role="img" aria-label="Photo of a smiling group in a bright room">
    <h2 class="cta__title">Stop wasting time and money<br>on treatments that don’t work.</h2>
    <p class="cta__text">People with diabetes have a shorter life expectancy of 10 years. Lifestyle medicine has been clinically proven to improve this, however the majority of information out there focuses only on insulin as the primary treatment. Even though there are more effective alternatives. You have nothing to lose and everything to gain by trying something different. Learn how to beat this disease for good — and get back to a life you love.</p>
    <span class="btn">Schedule a call</span>
  </section>

  <section class="signup">
    <h2 class="signup__title">3 Simple Steps to Take Control of Your Diabetes Today<br>(without spending any money)</h2>
    <div class="signup__form">
      <div class="field">First Name</div>
      <div class="field">Last Name</div>
      <div class="field">Email Address</div>
      <span class="btn">Submit</span>
    </div>
  </section>

  <footer class="site-footer">
    <div class="foot-brand">
      <span class="brand__dot" style="display:block"></span>
      <div class="brand__name">KESTREL HOLLOW</div>
      <p class="tiny">Lifestyle coaching that helps people reverse type 2 diabetes naturally and live fully again.</p>
      <div class="cards"><span></span><span></span><span></span><span></span></div>
    </div>
    <div>
      <div class="foot-title">UseFul Link</div>
      <ul class="foot-list"><li>Home</li><li>About</li><li>Service</li><li>High Risk</li><li>Method</li><li>Approach</li><li>Testimonial</li><li>Contact</li><li>Beating Diabetes</li></ul>
    </div>
    <div>
      <div class="foot-title">Quick Link</div>
      <ul class="foot-list"><li>PRIVACY POLICY</li><li>PHOTO POLICY</li><li>Term Condition</li><li>FAQS</li></ul>
    </div>
    <div>
      <div class="foot-title">News Letter</div>
      <p class="tiny">Get weekly recipes, coaching tips and stories from members who turned their health around.</p>
      <div class="news-input">Email Address</div>
      <div class="socials"><span></span><span class="on"></span><span></span><span></span></div>
    </div>
    <div>
      <div class="foot-title">REQUEST SERVICE</div>
      <div class="foot-label">Location</div>
      <p class="tiny">418 Willow Ridge Rd #12<br>Fairbank, Ohio 43210</p>
      <div class="foot-phone">702-555-0148</div>
      <p class="tiny">Call us for a free discovery chat about your goals, your habits and how we can help you.</p>
    </div>
    <div class="copy">Copy Right By Kestrel Hollow All Right Reserved 2022</div>
  </footer>
</main>

</body>
</html>
```